Pediatric Dentist Business Card

I need a business card designed for a dentist who works exclusively with children.
We prefer designs that are out of ordiary that is fun and interesting to kids.

there is no logo since this is a dentists office. The name of the doctor is "Tavor Kesh" if you want to get creative with that.

Target Market(s)

Kids

Industry/Entity Type

Business

Contact Information for Business Card

Anythings that is creative

Colors

Designer to choose colors to be used in the design.

```html
<!DOCTYPE html>
<html lang="en">
<head>
<meta charset="UTF-8">
<title>Pediatric Dentist Business Card</title>
<link href="https://fonts.googleapis.com/css2?family=Arimo:wght@700&family=Open+Sans:wght@400;600&display=swap" rel="stylesheet">
<style>
  :root {
    --canvas: #e9e6e1;
    --card: #ffffff;
    --brand-blue: #5689c8;
    --ink: #111111;
    --on-blue: #ffffff;
  }
  * { box-sizing: border-box; margin: 0; padding: 0; }
  html, body {
    width: 1200px;
    height: 1135px;
    overflow: hidden;
    background: var(--canvas);
  }
  .card {
    position: absolute;
    left: 237px;
    width: 679px;
    height: 406px;
    box-shadow: 0 6px 18px rgba(0, 0, 0, 0.18);
  }
  .card--front { top: 90px; background: var(--card); }
  .card--back { top: 625px; background: var(--brand-blue); }

  .side-band {
    position: absolute;
    left: 0; top: 0;
    width: 95px; height: 100%;
    background: var(--brand-blue);
  }
  .identity {
    position: absolute;
    left: 115px; top: 28px;
    color: var(--ink);
  }
  .identity__name {
    font-family: "Arimo", Arial, sans-serif;
    font-weight: 700;
    font-size: 15px;
    line-height: 18px;
  }
  .identity__title {
    font-family: "Open Sans", Arial, sans-serif;
    font-size: 13px;
    line-height: 20px;
  }
  .contact-list { list-style: none; }
  .contact-item {
    position: absolute;
    left: 0;
    width: 300px;
    height: 30px;
    display: flex;
    align-items: center;
  }
  .contact-item__icon {
    flex: 0 0 95px;
    display: flex;
    justify-content: center;
    padding-left: 20px;
  }
  .contact-item__icon svg { width: 24px; height: 24px; fill: var(--on-blue); }
  .contact-item__text {
    padding-left: 20px;
    font-family: "Open Sans", Arial, sans-serif;
    font-size: 14px;
    color: var(--ink);
    white-space: nowrap;
  }
  .contact-item--phone { top: 174px; }
  .contact-item--email { top: 234px; }
  .contact-item--web { top: 295px; }
  .contact-item--address { top: 354px; }

  .brand-mark {
    position: absolute;
    display: flex;
    align-items: center;
    gap: 10px;
    font-family: "Open Sans", Arial, sans-serif;
    font-weight: 600;
    white-space: nowrap;
  }
  .brand-mark__dot { border-radius: 50%; flex: none; }
  .card--front .brand-mark {
    left: 410px; top: 200px;
    font-size: 24px;
    color: var(--brand-blue);
  }
  .card--front .brand-mark__dot { width: 22px; height: 22px; background: var(--brand-blue); }
  .card--back .brand-mark {
    left: 0; width: 100%; top: 180px;
    justify-content: center;
    font-size: 34px;
    color: var(--on-blue);
  }
  .card--back .brand-mark__dot { width: 30px; height: 30px; background: var(--on-blue); }
</style>
</head>
<body>

<section class="card card--front">
  <div class="side-band"></div>

  <header class="identity">
    <h1 class="identity__name">Tavor Kesh</h1>
    <p class="identity__title">Pediatric Dentist</p>
  </header>

  <ul class="contact-list">
    <li class="contact-item contact-item--phone">
      <span class="contact-item__icon">
        <svg viewBox="0 0 24 24" aria-hidden="true"><path d="M6.6 2.5c.6-.4 1.4-.2 1.8.4l2 3.3c.3.6.2 1.3-.3 1.7l-1.3 1c.8 2.2 2.2 4.1 4 5.6l1.4-.9c.6-.4 1.3-.3 1.8.2l2.5 2.9c.4.5.4 1.3-.1 1.8l-1.6 1.5c-.8.7-2 .9-3 .4C9 18.2 5.3 13.2 4.3 7.5c-.2-1.1.2-2.2 1.1-2.9z"/></svg>
      </span>
      <span class="contact-item__text">(555) 014-2290</span>
    </li>
    <li class="contact-item contact-item--email">
      <span class="contact-item__icon">
        <svg viewBox="0 0 24 24" aria-hidden="true"><path d="M2 5h20v14H2z M3.5 6.5v.4l8.5 6 8.5-6v-.4z M3.5 8.7v8.8h17V8.7L12 14.6z" fill-rule="evenodd"/></svg>
      </span>
      <span class="contact-item__text">hello@brightbud.example</span>
    </li>
    <li class="contact-item contact-item--web">
      <span class="contact-item__icon">
        <svg viewBox="0 0 24 24" aria-hidden="true"><path fill="none" stroke="#fff" stroke-width="1.4" d="M12 2.5a9.5 9.5 0 1 0 0 19a9.5 9.5 0 1 0 0-19zM2.5 12h19M12 2.5c-3.2 3-3.2 16 0 19M12 2.5c3.2 3 3.2 16 0 19M4 7h16M4 17h16"/></svg>
      </span>
      <span class="contact-item__text">www.brightbud.example</span>
    </li>
    <li class="contact-item contact-item--address">
      <span class="contact-item__icon">
        <svg viewBox="0 0 24 24" aria-hidden="true"><path d="M12 1.5a7 7 0 0 0-7 7c0 5.2 7 14 7 14s7-8.8 7-14a7 7 0 0 0-7-7zm0 4a3 3 0 1 1 0 6a3 3 0 1 1 0-6z" fill-rule="evenodd"/></svg>
      </span>
      <span class="contact-item__text">12 Giggle Lane, Marlow</span>
    </li>
  </ul>

  <div class="brand-mark">
    <span class="brand-mark__dot"></span>
    <span class="brand-mark__name">Brightbud Dental</span>
  </div>
</section>

<section class="card card--back">
  <div class="brand-mark">
    <span class="brand-mark__dot"></span>
    <span class="brand-mark__name">Brightbud Dental</span>
  </div>
</section>

</body>
</html>
```